Redesign/Facelift for Affiliate Shopping Fashion Site

We are velunix, Fashion web site from Berlin, Germany,
looking to redesign/facelift our affiliate shopping site,
http://shop.velunix.de/bekleidung,27weky56okebmq37,ec_sale,sa
(Main page view)
http://shop.velunix.de/nordwerk-seidentunika-lisel,7uox9m8zsn2bq4j0,i
(Single article view)

Altogether we want to make it more coherent, key words being
MINIMAL and STYLISH.

NOTE:
You don´t need to completely design both pages, it would be sufficient to propose a direction you would take. However, we should be able to envision the complete solution.

The solution should be similar to another comparable affiliate site,
http://www.kaufzimt.de/browse/damen-kleidung

- - General Brief:
The design should have an overall aesthetic coherence,
especially when it comes to sizes of elements
and the bars like in the side bar left, or "Zum Shop".
The solution should be done for the main page and the single article page.

- - Here are the elements in particular, and how they should be designed:
- Main Page HEADER BAR (and single article page) elements:
header bar extends across the entire width of the screen
our logo
"Shopping" text next to the logo
search form
categories "Bekleidung, Accessoires, Schmuck" etc.
Facebook and twitter buttons

- Main page SIDEBAR (left):
elements as can be seen
menu "Preis" is replaced by a price "slider" to more accurately determine
a shopping price range

- Main page PRODUCTS:
elements as can be seen
the "% discount" symbol and "Zum Shop" elements especially
should be looked at

- Main page (and single article page) FOOTER:
should extend across the entire width of the screen

- Single article page
(http://shop.velunix.de/nordwerk-seidentunika-lisel,7uox9m8zsn2bq4j0,i)
header and footer as discussed for the Main page
bars (below the article) "Ähnliche Produkte zu….", "Weitere Produkte…" should be replaced by
"lighter" solution

Thank you,
feel free to ask question if something is not clear.
Kostis

```html
<!DOCTYPE html>
<html lang="de">
<head>
<meta charset="utf-8">
<title>Velunix Shopping – Bekleidung</title>
<link rel="stylesheet" href="https://fonts.googleapis.com/css2?family=Open+Sans:wght@400;600;700;800&family=Montserrat:wght@500&display=swap">
<style>
:root{
  --dark:#2b0e14;
  --darker:#220a0f;
  --red:#e8434f;
  --pink:#f07a83;
  --side:#f4f3f1;
  --line:#e4e2e0;
  --text:#4a4a4a;
  --muted:#9a9a9a;
  --white:#ffffff;
}
*{box-sizing:border-box;margin:0;padding:0}
html,body{width:998px;height:1200px;overflow:hidden}
body{position:relative;background:var(--white);font-family:'Open Sans',sans-serif;color:var(--text)}
a{color:inherit;text-decoration:none}

.site-header{position:absolute;left:0;top:0;width:998px;height:87px;background:var(--dark)}
.brand{position:absolute;left:130px;top:34px;display:flex;align-items:baseline;gap:8px;color:var(--white)}
.brand-name{font-weight:800;font-size:22px;letter-spacing:.5px}
.brand-tag{font-size:13px;font-weight:400}
.search{position:absolute;left:418px;top:35px;width:277px;height:28px;border-radius:14px;background:var(--white);font-size:9px;color:#777;padding:9px 0 0 17px}
.search svg{position:absolute;right:10px;top:6px}
.social{position:absolute;top:41px;display:flex;gap:4px;left:793px}
.social span{width:25px;height:25px;border-radius:50%;background:var(--white)}

.main-nav{position:absolute;left:0;top:87px;width:998px;height:39px;background:var(--red);display:flex;padding-left:133px;gap:16px;align-items:center}
.main-nav a{color:var(--white);font-size:12.4px;font-weight:600}

.sidebar{position:absolute;left:122px;top:146px;width:170px;height:460px;background:var(--side);border-radius:3px}
.sidebar h3{font-size:10.4px;font-weight:700;color:#222;padding:15px 0 0 22px;height:35px;border-bottom:1px solid var(--line)}
.cat-active{font-size:10.5px;color:#444;padding:6px 0 0 20px}
.cat-active svg{vertical-align:middle;margin-right:2px}
.subcats{list-style:none;margin-top:6px}
.subcats li{display:flex;font-size:8.6px;height:19.1px;align-items:center;padding-left:35px}
.subcats li span:first-child{width:79px;color:#555}
.subcats li span:last-child{color:var(--muted)}
.filters{list-style:none;margin-top:4px}
.filters li{height:25px;border-bottom:1px solid var(--line);display:flex;align-items:center;justify-content:space-between;padding:0 14px 0 22px;font-size:10.3px;font-weight:600;color:#222}
.filters li:last-child{border-bottom:none}

.sort{position:absolute;left:762px;top:140px;width:113px;height:28px;border:1px solid #ddd;background:#f6f6f6;font-size:10.5px;color:#777;padding:6px 0 0 11px}
.sort svg{position:absolute;right:10px;top:11px}

.products{position:absolute;left:320px;top:172px;width:560px}
.row{display:flex;height:267px;border-bottom:1px solid var(--line);position:relative}
.row:last-child{border-bottom:none}
.card{width:144px;position:relative}
.photo{width:110px;height:135px;margin-left:12px;border-radius:4px}
.title{position:absolute;top:152px;left:0;font-size:9.6px;color:#555;white-space:nowrap}
.price{position:absolute;top:168px;left:0;font-size:10px}
.price s{color:#444;font-size:9px}
.price b{color:var(--red);font-weight:400;margin-left:3px}
.actions{position:absolute;top:184px;left:0;display:flex;gap:7px}
.to-shop{width:79px;height:24px;background:var(--red);color:var(--white);font-size:9.6px;display:flex;align-items:center;justify-content:center;gap:4px}
.discount{position:relative;width:33px;height:22px;margin-top:1px;background:var(--pink);color:var(--white);font-size:11px;display:flex;align-items:center;justify-content:center}
.discount::before{content:"";position:absolute;left:8px;top:-8px;border-left:0 solid transparent;border-right:10px solid transparent;border-bottom:8px solid var(--pink)}
.row .card:nth-child(n){}
.row.second .card,.row.third .card{left:2px}

.site-footer{position:absolute;left:0;top:952px;width:998px;height:248px;background:var(--dark);border-top:4px solid var(--red)}
.footer-col{position:absolute;top:34px}
.footer-col h4{font-family:'Montserrat',sans-serif;font-weight:500;font-size:13px;color:var(--white);margin-bottom:8px;letter-spacing:.3px}
.footer-col ul{list-style:none}
.footer-col li{font-size:10px;color:var(--white);height:18.4px}
.footer-brand{position:absolute;left:734px;top:68px;color:var(--white);font-weight:800;font-size:22px;letter-spacing:.5px}
.footer-bottom{position:absolute;left:0;top:192px;width:998px;height:52px;background:var(--darker)}
.copyright{position:absolute;left:139px;top:18px;font-size:9px;color:#999}
.footer-social{position:absolute;left:799px;top:18px;display:flex;gap:5px}
.footer-social span{width:16px;height:15px;border-radius:2px}
</style>
</head>
<body>
<header class="site-header">
  <a class="brand" href="#"><span class="brand-name">VELUNIX</span><span class="brand-tag">SHOPPING</span></a>
  <div class="search">Bekleidung, Accessoires, Schmuck etc.
    <svg width="16" height="16" viewBox="0 0 16 16"><circle cx="7" cy="7" r="5.5" fill="none" stroke="#999" stroke-width="1.4"/><line x1="11" y1="11" x2="15" y2="15" stroke="#999" stroke-width="1.6"/></svg>
  </div>
  <div class="social" aria-label="Soziale Netzwerke"><span></span><span></span></div>
</header>

<nav class="main-nav">
  <a href="#">Bekleidung</a><a href="#">Accessoires</a><a href="#">Schmuck</a><a href="#">Schuhe</a><a href="#">Taschen</a><a href="#">Uhren</a><a href="#">Beauty</a><a href="#">Wohnen</a><a href="#">Haushalt</a><a href="#">Drogerie</a><a href="#">Sport und Freizeit</a>
</nav>

<aside class="sidebar">
  <h3>CATEGORY</h3>
  <div class="cat-active"><svg width="10" height="9" viewBox="0 0 10 9"><path d="M1 5l3 3 5-7" fill="none" stroke="#e8434f" stroke-width="1.8"/></svg>Bekleidung</div>
  <ul class="subcats">
    <li><span>Anzüge</span><span>(135)</span></li>
    <li><span>Bademode</span><span>(4477)</span></li>
    <li><span>Blazer</span><span>(1133)</span></li>
    <li><span>Blusen</span><span>(3128)</span></li>
    <li><span>Wäsche</span><span>(3652)</span></li>
    <li><span>Hemden</span><span>(7988)</span></li>
    <li><span>Homewear</span><span>(100)</span></li>
    <li><span>Hosen</span><span>(43168)</span></li>
    <li><span>Jacken</span><span>(15783)</span></li>
    <li><span>Jeans</span><span>(17207)</span></li>
    <li><span>Kleider</span><span>(32160)</span></li>
  </ul>
  <ul class="filters">
    <li>MARKEN<svg width="6" height="9" viewBox="0 0 6 9"><path d="M0 0l6 4.5L0 9z" fill="#e8434f"/></svg></li>
    <li>PRICE<svg width="6" height="9" viewBox="0 0 6 9"><path d="M0 0l6 4.5L0 9z" fill="#e8434f"/></svg></li>
    <li>SALE<svg width="6" height="9" viewBox="0 0 6 9"><path d="M0 0l6 4.5L0 9z" fill="#e8434f"/></svg></li>
    <li>FARBE<svg width="6" height="9" viewBox="0 0 6 9"><path d="M0 0l6 4.5L0 9z" fill="#e8434f"/></svg></li>
    <li>MATERIAL<svg width="6" height="9" viewBox="0 0 6 9"><path d="M0 0l6 4.5L0 9z" fill="#e8434f"/></svg></li>
    <li>MUSTER<svg width="6" height="9" viewBox="0 0 6 9"><path d="M0 0l6 4.5L0 9z" fill="#e8434f"/></svg></li>
    <li>SHOPS<svg width="6" height="9" viewBox="0 0 6 9"><path d="M0 0l6 4.5L0 9z" fill="#e8434f"/></svg></li>
  </ul>
</aside>

<div class="sort">Relevance by<svg width="9" height="6" viewBox="0 0 9 6"><path d="M0 0h9L4.5 6z" fill="#777"/></svg></div>

<main class="products">
  <div class="row">
    <div class="card"><div class="photo" role="img" aria-label="Gelbes ärmelloses Kleid" style="background:linear-gradient(#fff 0%,#f1ea5a 20%,#ebe34c 100%)"></div><p class="title">LORANO Cardigan aus Leinen</p><p class="price"><s>35.99€</s><b>24.99 € *</b></p><div class="actions"><a class="to-shop" href="#"><svg width="12" height="11" viewBox="0 0 12 11"><rect x="1" y="3" width="10" height="7.5" fill="none" stroke="#fff" stroke-width="1.3"/><path d="M4 3V1.5h4V3" fill="none" stroke="#fff" stroke-width="1.3"/></svg>Zum Shop</a><span class="discount">-31%</span></div></div>
    <div class="card"><div class="photo" role="img" aria-label="Cremefarbener Blazer" style="background:linear-gradient(#efe8db,#e4dccb)"></div><p class="title">LORANO Cardigan aus Leinen</p><p class="price"><s>35.99€</s><b>24.99 € *</b></p><div class="actions"><a class="to-shop" href="#"><svg width="12" height="11" viewBox="0 0 12 11"><rect x="1" y="3" width="10" height="7.5" fill="none" stroke="#fff" stroke-width="1.3"/><path d="M4 3V1.5h4V3" fill="none" stroke="#fff" stroke-width="1.3"/></svg>Zum Shop</a><span class="discount">-31%</span></div></div>
    <div class="card"><div class="photo" role="img" aria-label="Dunkelrotes Spitzenkleid" style="background:linear-gradient(#fff 0%,#5a2a35 15%,#4a1f2a 100%)"></div><p class="title">LORANO Cardigan aus Leinen</p><p class="price"><s>35.99€</s><b>24.99 € *</b></p><div class="actions"><a class="to-shop" href="#"><svg width="12" height="11" viewBox="0 0 12 11"><rect x="1" y="3" width="10" height="7.5" fill="none" stroke="#fff" stroke-width="1.3"/><path d="M4 3V1.5h4V3" fill="none" stroke="#fff" stroke-width="1.3"/></svg>Zum Shop</a><span class="discount">-31%</span></div></div>
    <div class="card"><div class="photo" role="img" aria-label="Graublaue Jacke" style="background:linear-gradient(#8c99a8,#7a8797)"></div><p class="title">LORANO Cardigan aus Leinen</p><p class="price"><s>35.99€</s><b>24.99 € *</b></p><div class="actions"><a class="to-shop" href="#"><svg width="12" height="11" viewBox="0 0 12 11"><rect x="1" y="3" width="10" height="7.5" fill="none" stroke="#fff" stroke-width="1.3"/><path d="M4 3V1.5h4V3" fill="none" stroke="#fff" stroke-width="1.3"/></svg>Zum Shop</a><span class="discount">-31%</span></div></div>
  </div>
  <div class="row second">
    <div class="card"><div class="photo" role="img" aria-label="Schwarze Lederjacke" style="background:linear-gradient(#2a2a2a,#161616);margin-top:90px;height:1px;position:absolute;opacity:0"></div><div class="photo" role="img" aria-label="Schwarze Lederjacke" style="background:linear-gradient(#2a2a2a,#141414);margin-top:0"></div><p class="title">LORANO Cardigan aus Leinen</p><p class="price"><s>35.99€</s><b>24.99 € *</b></p><div class="actions"><a class="to-shop" href="#"><svg width="12" height="11" viewBox="0 0 12 11"><rect x="1" y="3" width="10" height="7.5" fill="none" stroke="#fff" stroke-width="1.3"/><path d="M4 3V1.5h4V3" fill="none" stroke="#fff" stroke-width="1.3"/></svg>Zum Shop</a><span class="discount">-31%</span></div></div>
    <div class="card"><div class="photo" role="img" aria-label="Helles fliederfarbenes Abendkleid" style="background:linear-gradient(#ebe4ea,#d9cfd8)"></div><p class="title">LORANO Cardigan aus Leinen</p><p class="price"><s>35.99€</s><b>24.99 € *</b></p><div class="actions"><a class="to-shop" href="#"><svg width="12" height="11" viewBox="0 0 12 11"><rect x="1" y="3" width="10" height="7.5" fill="none" stroke="#fff" stroke-width="1.3"/><path d="M4 3V1.5h4V3" fill="none" stroke="#fff" stroke-width="1.3"/></svg>Zum Shop</a><span class="discount">-31%</span></div></div>
    <div class="card"><div class="photo" role="img" aria-label="Rotes Neckholder-Kleid" style="background:linear-gradient(#f04a36,#d9301f)"></div><p class="title">LORANO Cardigan aus Leinen</p><p class="price"><s>35.99€</s><b>24.99 € *</b></p><div class="actions"><a class="to-shop" href="#"><svg width="12" height="11" viewBox="0 0 12 11"><rect x="1" y="3" width="10" height="7.5" fill="none" stroke="#fff" stroke-width="1.3"/><path d="M4 3V1.5h4V3" fill="none" stroke="#fff" stroke-width="1.3"/></svg>Zum Shop</a><span class="discount">-31%</span></div></div>
    <div class="card"><div class="photo" role="img" aria-label="Weiß-hellblaues Spitzenkleid" style="background:linear-gradient(#eef5f8,#c8e2ec)"></div><p class="title">LORANO Cardigan aus Leinen</p><p class="price"><s>35.99€</s><b>24.99 € *</b></p><div class="actions"><a class="to-shop" href="#"><svg width="12" height="11" viewBox="0 0 12 11"><rect x="1" y="3" width="10" height="7.5" fill="none" stroke="#fff" stroke-width="1.3"/><path d="M4 3V1.5h4V3" fill="none" stroke="#fff" stroke-width="1.3"/></svg>Zum Shop</a><span class="discount">-31%</span></div></div>
  </div>
  <div class="row third">
    <div class="card"><div class="photo" role="img" aria-label="Gemusterte Shorts" style="background:linear-gradient(#c4bfba,#a9a39d)"></div><p class="title">LORANO Cardigan aus Leinen</p><p class="price"><s>35.99€</s><b>24.99 € *</b></p><div class="actions"><a class="to-shop" href="#"><svg width="12" height="11" viewBox="0 0 12 11"><rect x="1" y="3" width="10" height="7.5" fill="none" stroke="#fff" stroke-width="1.3"/><path d="M4 3V1.5h4V3" fill="none" stroke="#fff" stroke-width="1.3"/></svg>Zum Shop</a><span class="discount">-31%</span></div></div>
    <div class="card"><div class="photo" role="img" aria-label="Weiße Lederjacke" style="background:linear-gradient(#f2f2f0,#dcdcda)"></div><p class="title">LORANO Cardigan aus Leinen</p><p class="price"><s>35.99€</s><b>24.99 € *</b></p><div class="actions"><a class="to-shop" href="#"><svg width="12" height="11" viewBox="0 0 12 11"><rect x="1" y="3" width="10" height="7.5" fill="none" stroke="#fff" stroke-width="1.3"/><path d="M4 3V1.5h4V3" fill="none" stroke="#fff" stroke-width="1.3"/></svg>Zum Shop</a><span class="discount">-31%</span></div></div>
    <div class="card"><div class="photo" role="img" aria-label="Smaragdgrünes langes Kleid" style="background:linear-gradient(#17967c,#0f7a63)"></div><p class="title">LORANO Cardigan aus Leinen</p><p class="price"><s>35.99€</s><b>24.99 € *</b></p><div class="actions"><a class="to-shop" href="#"><svg width="12" height="11" viewBox="0 0 12 11"><rect x="1" y="3" width="10" height="7.5" fill="none" stroke="#fff" stroke-width="1.3"/><path d="M4 3V1.5h4V3" fill="none" stroke="#fff" stroke-width="1.3"/></svg>Zum Shop</a><span class="discount">-31%</span></div></div>
    <div class="card"><div class="photo" role="img" aria-label="Gemusterte helle Stoffhose" style="background:linear-gradient(#d8d2c8,#bfb7aa)"></div><p class="title">LORANO Cardigan aus Leinen</p><p class="price"><s>35.99€</s><b>24.99 € *</b></p><div class="actions"><a class="to-shop" href="#"><svg width="12" height="11" viewBox="0 0 12 11"><rect x="1" y="3" width="10" height="7.5" fill="none" stroke="#fff" stroke-width="1.3"/><path d="M4 3V1.5h4V3" fill="none" stroke="#fff" stroke-width="1.3"/></svg>Zum Shop</a><span class="discount">-31%</span></div></div>
  </div>
</main>

<footer class="site-footer">
  <div class="footer-col" style="left:131px"><h4>COMPANY</h4><ul><li>Home</li><li>About Us</li><li>Career</li><li>Partial Client List</li><li>Corporate Programs</li></ul></div>
  <div class="footer-col" style="left:279px"><h4>PRODUCTS</h4><ul><li>Phasellus felis</li><li>Dolor scelerisque</li><li>Tempus eget lobortis</li><li>Donec scelerisque</li><li>Leo ac risus</li></ul></div>
  <div class="footer-col" style="left:434px"><h4>SPECIALS</h4><ul><li>Phasellus felis</li><li>Dolor scelerisque</li><li>Tempus eget lobortis</li><li>Donec scelerisque</li><li>Leo ac risus</li></ul></div>
  <div class="footer-col" style="left:581px"><h4>SUPPORT</h4><ul><li>Phasellus felis</li><li>Dolor scelerisque</li><li>Tempus eget lobortis</li><li>Donec scelerisque</li><li>Leo ac risus</li></ul></div>
  <div class="footer-brand">VELUNIX</div>
  <div class="footer-bottom">
    <p class="copyright">© 2014 Company Name.&nbsp; All right reserved.&nbsp; Term of Use</p>
    <div class="footer-social" aria-label="Soziale Netzwerke"><span style="background:#3b5a9a"></span><span style="background:#3fb2e2"></span><span style="background:#1f7ab8"></span><span style="background:#f28a1e"></span></div>
  </div>
</footer>
</body>
</html>
```